SHIPPING ONE

SHIPPING

Reason: I need a better balance between services - we have four main services - my inability to make that clear is the reason for the extenison- The four services are 1- Warehousing 2- ZUL Certified - Braxley Customs Clearance and all the PGA's (Participating Government Agencies) that comprise products imported into the United States 3- Trucking - our own trucks and 3 PL (third Party Logistics) 4- Export - Ocean Freight (NVOCC) AND Air freight (OWRK)

Target Market(s)

U.S. IMPORTERS

Industry/Entity Type

Shipping

Requirements
Must have
• LOGO AND ADDRESS
• WEB SITE - WWW.KELLAND-CARGO.COM
Nice to have
• WAREHOUSE Services
• Carton Pick
• Palletization
• Pallet re-build
• Transporation Services
• CONTAINER STRIPPING

```html
<!DOCTYPE html>
<html lang="en">
<head>
<meta charset="utf-8">
<title>Kelland Cargo Postcard</title>
<link href="https://fonts.googleapis.com/css2?family=Roboto+Condensed:wght@700&display=swap" rel="stylesheet">
<style>
  :root {
    --brand-blue: #052bc4;
    --edge-grey: #8c9c9a;
    --pill-grey: #b4bab8;
    --pill-shade: #6f7674;
    --accent-red: #a0070b;
    --text-white: #ffffff;
    --postal-grey: #e0e0e0;
    --paper: #ffffff;
  }
  * { margin: 0; padding: 0; box-sizing: border-box; }
  html, body { width: 1200px; height: 930px; overflow: hidden; background: var(--paper); }
  .postcard {
    position: relative;
    width: 1200px;
    height: 930px;
    overflow: hidden;
    background: var(--paper);
    font-family: "Roboto Condensed", "Arial Narrow", sans-serif;
    font-weight: 700;
  }
  .postcard__art { position: absolute; inset: 0; }
  .services { position: absolute; left: 0; top: 0; width: 510px; height: 930px; }
  .services__line {
    position: absolute;
    left: 0;
    width: 510px;
    text-align: center;
    color: var(--text-white);
    font-size: 22px;
    letter-spacing: 3px;
    line-height: 1;
    white-space: nowrap;
  }
  .services__logo { top: 64px; left: -38px; font-size: 23px; }
  .services__contact { top: 846px; left: -10px; }
  .services__web { top: 880px; left: -10px; font-size: 20px; letter-spacing: 2.4px; }
  .pill {
    position: absolute;
    left: 95px;
    width: 320px;
    height: 54px;
    display: flex;
    align-items: center;
    justify-content: center;
    border-radius: 30px;
    background: radial-gradient(ellipse at center, var(--pill-grey) 55%, var(--pill-shade) 100%);
    color: var(--accent-red);
    font-size: 23px;
    letter-spacing: 3px;
    white-space: nowrap;
  }
</style>
</head>
<body>
<main class="postcard">
  <svg class="postcard__art" width="1200" height="930" viewBox="0 0 1200 930" aria-hidden="true">
    <ellipse class="panel-edge" cx="0" cy="505" rx="610" ry="676" fill="var(--edge-grey)"/>
    <ellipse class="panel" cx="-2" cy="505" rx="604" ry="674" fill="var(--brand-blue)"/>
    <rect class="stamp-box" x="934" y="119" width="133" height="152" fill="none" stroke="var(--postal-grey)" stroke-width="8"/>
    <g class="address-lines" stroke="var(--postal-grey)" stroke-width="8" stroke-linecap="round" stroke-dasharray="0 17.5">
      <line x1="713" y1="492" x2="1100" y2="492"/>
      <line x1="713" y1="585" x2="1100" y2="585"/>
      <line x1="713" y1="685" x2="1100" y2="685"/>
    </g>
  </svg>

  <section class="services">
    <p class="services__line services__logo">LOGO?</p>

    <h2 class="pill" style="top:140px">WAREHOUSE Services</h2>
    <p class="services__line" style="top:214px">Carton Pick</p>
    <p class="services__line" style="top:245px">Palletization</p>
    <p class="services__line" style="top:276px">Pallet re-build</p>

    <h2 class="pill" style="top:320px">CUSTOMS CLEARANCE</h2>
    <p class="services__line" style="top:394px">BRAXLEY CUSTOMS</p>
    <p class="services__line" style="top:425px">ZUL CERTIFIED</p>
    <p class="services__line" style="top:456px">ALL PGA'S</p>

    <h2 class="pill" style="top:500px">TRUCKING</h2>
    <p class="services__line" style="top:574px">Our Own Trucks</p>
    <p class="services__line" style="top:605px">3PL Logistics</p>
    <p class="services__line" style="top:636px">CONTAINER STRIPPING</p>

    <h2 class="pill" style="top:680px">EXPORT AIR AND OCEAN</h2>
    <p class="services__line" style="top:754px">Ocean Freight NVOCC</p>
    <p class="services__line" style="top:785px">Air Freight OWRK</p>

    <p class="services__line services__contact">CONTACT INFO?</p>
    <p class="services__line services__web">WWW.KELLAND-CARGO.COM</p>
  </section>
</main>
</body>
</html>
```